Awesome WYSIWYG

I'm looking for someone to redesign this WYSIWYG Editor that I've developed. I'm looking for a really cool and modern design that will leave my clients stunned. Hopefully, this tool will be embedded into a software package which is currently used around the world.
I need to add a character count to the design and I would like my logo incorporated somewhere into the design as well. Otherwise, I'm not fussed about the layout, feel free to move elements around.
I'm expecting that the designer will provide all icons, color codes and anything else I will need to recreate the design exactly within my development environment.
This is an example of the type of wow I'm looking for:
https://pixelvane.example/shots/4826317-Clean-Minimal-Rich-Text-Panel-Kit
I'm happy to receive the icon files in vector format or high quality jpg. Ideally vectors would be best. At a guess, I expect the icons will need to be scaled to as big as 30px square.
Icons Needed: Set BG Color, set font color, create hyperlink, remove hyperlink, QuillPeak IT logo (links to my website), cut, copy, paste, bold, underline, italic, text align left, text align center, text justify, text align right, indent line, outdent line, bulleted list, numbered list, save button (currently just has text "update changes")

```html
<!DOCTYPE html>
<html lang="en">
<head>
<meta charset="utf-8">
<title>QuillPeak IT WYSIWYG editor UI – sliced assets</title>
<link href="https://fonts.googleapis.com/css2?family=Mulish:wght@400;600;700;800&display=swap" rel="stylesheet">
<style>
  :root{
    --blue:#0b95d9;
    --blue-dark:#06679b;
    --divider:#3aacE3;
    --sheet:#f3f3f3;
    --page:#ffffff;
    --ink:#111111;
    --grey-text:#444444;
    --field-border:#8a8a8a;
    --muted:#9a9a9a;
    --link-grey:#666666;
    --swatch:#f26a2a;
    --black:#000000;
    --white:#ffffff;
  }
  *{box-sizing:border-box;margin:0;padding:0}
  html,body{width:1200px;height:1000px;overflow:hidden;background:var(--page);font-family:"Mulish",sans-serif}
  .canvas{position:relative;width:1200px;height:1000px}
  .asset-sheet{position:absolute;left:0;top:0;width:1200px;height:460px;background:var(--sheet)}
  .size-label{position:absolute;left:174px;font-size:18px;color:var(--ink);display:flex;align-items:center;gap:4px}
  .size-label b{font-weight:700}
  .size-label::after{content:"";position:absolute;left:57px;top:0;bottom:0;width:2px;background:var(--ink)}
  .row{position:absolute;left:263px;display:flex;gap:10px}
  .tool{width:36px;height:36px;border-radius:3px;display:flex;align-items:center;justify-content:center;color:var(--white);font-size:15px;font-weight:700}
  .tool svg{width:14px;height:14px}
  .row--normal .tool{background:var(--blue)}
  .row--active .tool{background:var(--blue-dark)}
  .bar-cap{width:10px;height:36px;background:var(--blue)}
  .bar-cap--left{border-radius:3px 0 0 3px}
  .bar-cap--right{border-radius:0 3px 3px 0}
  .ital{font-style:italic;font-weight:700}
  .under{text-decoration:underline;font-weight:600;text-underline-offset:2px}

  .control{height:28px;border-radius:3px;display:flex;align-items:center;justify-content:center}
  .control svg{width:14px;height:14px}
  .field{border:1px solid var(--field-border);background:var(--white);color:var(--grey-text);font-size:12px;font-weight:600;letter-spacing:.5px;justify-content:space-between;padding:0 10px}
  .caret{width:0;height:0;border-left:4px solid transparent;border-right:4px solid transparent;border-top:4px solid var(--grey-text)}
  .square{width:28px}
  .square--outline{border:1px solid var(--field-border);background:var(--white);color:var(--grey-text)}
  .square--black{background:var(--black);color:var(--white)}
  .square--grey{background:var(--link-grey);color:var(--white)}
  .swatch-chip{width:14px;height:14px;border-radius:3px;background:var(--white)}
  .swatch-chip--orange{width:18px;height:18px;background:var(--swatch)}
  .font-a{display:flex;flex-direction:column;align-items:center;font-weight:800;font-size:14px;line-height:12px}
  .font-a::after{content:"";width:12px;height:2px;background:currentColor;margin-top:1px}

  .credit{display:flex;flex-direction:column;align-items:flex-end;color:var(--muted);line-height:9px}
  .credit small{font-size:8px;font-weight:600}
  .credit span{font-size:9px;font-weight:800;display:flex;align-items:center;gap:4px}
  .credit span::after{content:"";width:14px;height:14px;border-radius:50%;border:1.5px solid var(--muted)}

  .editor-bar{position:absolute;left:263px;top:560px;width:534px;height:36px;background:var(--blue);border-radius:4px;display:flex;overflow:hidden}
  .editor-bar .tool{border-radius:0;background:transparent}
  .editor-bar .tool.is-active{background:var(--blue-dark)}
  .editor-bar .group{display:flex;border-right:1px solid var(--divider)}
  .editor-bar .group:last-child{border-right:none}
  .editor-options{position:absolute;left:263px;top:600px;width:534px;display:flex;gap:4px}
  .editor-options .field{margin-right:1px}

  .caption{position:absolute;left:0;width:1200px;text-align:center}
  .caption h1{font-size:24px;font-weight:400;color:var(--blue);letter-spacing:.5px;margin-top:880px}
  .caption h1 strong{font-weight:700}
  .caption p{font-size:15px;font-weight:700;color:var(--grey-text);letter-spacing:.6px}
</style>
</head>
<body>
<svg width="0" height="0" style="position:absolute" aria-hidden="true">
  <defs>
    <symbol id="i-left" viewBox="0 0 16 16" fill="currentColor"><rect x="2" y="2" width="12" height="1.6"/><rect x="2" y="5.5" width="8" height="1.6"/><rect x="2" y="9" width="12" height="1.6"/><rect x="2" y="12.5" width="8" height="1.6"/></symbol>
    <symbol id="i-center" viewBox="0 0 16 16" fill="currentColor"><rect x="2" y="2" width="12" height="1.6"/><rect x="4" y="5.5" width="8" height="1.6"/><rect x="2" y="9" width="12" height="1.6"/><rect x="4" y="12.5" width="8" height="1.6"/></symbol>
    <symbol id="i-right" viewBox="0 0 16 16" fill="currentColor"><rect x="2" y="2" width="12" height="1.6"/><rect x="6" y="5.5" width="8" height="1.6"/><rect x="2" y="9" width="12" height="1.6"/><rect x="6" y="12.5" width="8" height="1.6"/></symbol>
    <symbol id="i-justify" viewBox="0 0 16 16" fill="currentColor"><rect x="2" y="1.5" width="12" height="1.5"/><rect x="2" y="4.5" width="12" height="1.5"/><rect x="2" y="7.5" width="12" height="1.5"/><rect x="2" y="10.5" width="12" height="1.5"/><rect x="2" y="13.5" width="12" height="1.5"/></symbol>
    <symbol id="i-indent" viewBox="0 0 16 16" fill="currentColor"><path d="M1 5.5 4.5 8 1 10.5z"/><rect x="6" y="2" width="1.4" height="12"/><rect x="8.5" y="2.5" width="6" height="1.5"/><rect x="8.5" y="6" width="4.5" height="1.5"/><rect x="8.5" y="9.5" width="6" height="1.5"/><rect x="8.5" y="13" width="4.5" height="1.5"/></symbol>
    <symbol id="i-outdent" viewBox="0 0 16 16" fill="currentColor"><rect x="1.5" y="2.5" width="6" height="1.5"/><rect x="1.5" y="6" width="4.5" height="1.5"/><rect x="1.5" y="9.5" width="6" height="1.5"/><rect x="1.5" y="13" width="4.5" height="1.5"/><rect x="9" y="2" width="1.4" height="12"/><path d="M15 5.5 11.5 8 15 10.5z"/></symbol>
    <symbol id="i-bullets" viewBox="0 0 16 16" fill="currentColor"><circle cx="2.5" cy="3.5" r="1.4"/><circle cx="2.5" cy="8" r="1.4"/><circle cx="2.5" cy="12.5" r="1.4"/><rect x="5.5" y="2.8" width="9.5" height="1.5"/><rect x="5.5" y="7.3" width="9.5" height="1.5"/><rect x="5.5" y="11.8" width="9.5" height="1.5"/></symbol>
    <symbol id="i-numbers" viewBox="0 0 16 16" fill="currentColor"><rect x="2" y="2" width="1" height="3"/><rect x="1.5" y="6.5" width="2" height="0.9"/><rect x="2.5" y="7.4" width="1" height="1.2"/><rect x="1.5" y="8.6" width="2" height="0.9"/><rect x="1.5" y="11" width="2" height="0.9"/><rect x="1.5" y="12.5" width="2" height="0.9"/><rect x="1.5" y="14" width="2" height="0.9"/><rect x="5.5" y="2.8" width="9.5" height="1.5"/><rect x="5.5" y="7.3" width="9.5" height="1.5"/><rect x="5.5" y="11.8" width="9.5" height="1.5"/></symbol>
    <symbol id="i-cut" viewBox="0 0 16 16" fill="none" stroke="currentColor" stroke-width="1.6"><circle cx="4.5" cy="12" r="2.2"/><circle cx="11.5" cy="12" r="2.2"/><path d="M5.6 10 10.5 2M10.4 10 5.5 2"/></symbol>
    <symbol id="i-copy" viewBox="0 0 16 16" fill="none" stroke="currentColor" stroke-width="1.6"><rect x="5.5" y="5.5" width="8" height="8" rx="1.5"/><path d="M10.5 3.5V3a1 1 0 0 0-1-1H3a1 1 0 0 0-1 1v6.5a1 1 0 0 0 1 1h.5"/></symbol>
    <symbol id="i-paste" viewBox="0 0 16 16"><rect x="2.3" y="2.3" width="10" height="10" rx="2" fill="none" stroke="currentColor" stroke-width="1.6"/><rect x="6" y="6.5" width="8" height="7" rx="1" fill="currentColor"/></symbol>
    <symbol id="i-link" viewBox="0 0 16 16" fill="none" stroke="currentColor" stroke-width="1.8" stroke-linecap="round"><path d="M7 9a3 3 0 0 0 4.2 0l2.1-2.1a3 3 0 0 0-4.2-4.2L8.3 3.5"/><path d="M9 7a3 3 0 0 0-4.2 0L2.7 9.1a3 3 0 0 0 4.2 4.2l.8-.8"/></symbol>
  </defs>
</svg>

<main class="canvas">
  <section class="asset-sheet" aria-label="Sliced toolbar assets">
    <div class="size-label" style="top:240px;height:36px"><b>36</b> px</div>
    <div class="row row--normal" style="top:240px">
      <div class="tool">B</div>
      <div class="tool ital">i</div>
      <div class="tool under">U</div>
      <div class="tool"><svg><use href="#i-left"/></svg></div>
      <div class="tool"><svg><use href="#i-center"/></svg></div>
      <div class="tool"><svg><use href="#i-right"/></svg></div>
      <div class="tool"><svg><use href="#i-justify"/></svg></div>
      <div class="tool"><svg><use href="#i-indent"/></svg></div>
      <div class="tool"><svg><use href="#i-outdent"/></svg></div>
      <div class="tool"><svg><use href="#i-bullets"/></svg></div>
      <div class="tool"><svg><use href="#i-numbers"/></svg></div>
      <div class="tool"><svg><use href="#i-cut"/></svg></div>
      <div class="tool"><svg><use href="#i-copy"/></svg></div>
      <div class="tool"><svg><use href="#i-paste"/></svg></div>
      <div class="bar-cap bar-cap--left"></div>
      <div class="bar-cap bar-cap--right"></div>
    </div>

    <div class="size-label" style="top:286px;height:36px"><b>36</b> px</div>
    <div class="row row--active" style="top:286px">
      <div class="tool">B</div>
      <div class="tool ital">i</div>
      <div class="tool under">U</div>
      <div class="tool"><svg><use href="#i-left"/></svg></div>
      <div class="tool"><svg><use href="#i-center"/></svg></div>
      <div class="tool"><svg><use href="#i-right"/></svg></div>
      <div class="tool"><svg><use href="#i-justify"/></svg></div>
      <div class="tool"><svg><use href="#i-indent"/></svg></div>
      <div class="tool"><svg><use href="#i-outdent"/></svg></div>
      <div class="tool"><svg><use href="#i-bullets"/></svg></div>
      <div class="tool"><svg><use href="#i-numbers"/></svg></div>
      <div class="tool"><svg><use href="#i-cut"/></svg></div>
      <div class="tool"><svg><use href="#i-copy"/></svg></div>
      <div class="tool"><svg><use href="#i-paste"/></svg></div>
    </div>

    <div class="size-label" style="top:332px;height:28px"><b>28</b> px</div>
    <div class="row" style="top:332px;align-items:center">
      <div class="control field" style="width:68px;justify-content:flex-end"><span class="caret"></span></div>
      <div class="control square square--outline"></div>
      <div class="control square square--black"><span class="swatch-chip"></span></div>
      <div class="control square square--black"><span class="font-a">A</span></div>
      <div class="control square square--outline"><svg><use href="#i-link"/></svg></div>
      <div class="control square square--grey"><svg><use href="#i-link"/></svg></div>
      <div class="credit" style="margin-left:7px"><small>brought by</small><span>QuillPeak IT</span></div>
    </div>
  </section>

  <section class="editor-preview" aria-label="Assembled editor toolbar">
    <div class="editor-bar">
      <div class="group">
        <div class="tool">B</div>
        <div class="tool ital">i</div>
        <div class="tool under">U</div>
        <div class="tool is-active"><svg><use href="#i-left"/></svg></div>
        <div class="tool"><svg><use href="#i-center"/></svg></div>
        <div class="tool"><svg><use href="#i-right"/></svg></div>
        <div class="tool"><svg><use href="#i-justify"/></svg></div>
      </div>
      <div class="group">
        <div class="tool"><svg><use href="#i-indent"/></svg></div>
        <div class="tool"><svg><use href="#i-outdent"/></svg></div>
        <div class="tool"><svg><use href="#i-bullets"/></svg></div>
        <div class="tool"><svg><use href="#i-numbers"/></svg></div>
      </div>
      <div class="group">
        <div class="tool"><svg><use href="#i-cut"/></svg></div>
        <div class="tool"><svg><use href="#i-copy"/></svg></div>
        <div class="tool"><svg><use href="#i-paste"/></svg></div>
      </div>
    </div>
    <div class="editor-options">
      <div class="control field" style="width:160px">Times New Roman <span class="caret"></span></div>
      <div class="control field" style="width:80px">16 pt <span class="caret"></span></div>
      <div class="control square square--outline"><span class="swatch-chip swatch-chip--orange"></span></div>
      <div class="control square square--outline"><span class="font-a">A</span></div>
      <div class="control square square--grey"><svg><use href="#i-link"/></svg></div>
      <div class="credit" style="margin-left:auto"><small>brought by</small><span>QuillPeak IT</span></div>
    </div>
  </section>

  <header class="caption">
    <h1><strong>sliced assets</strong> (100% pixel size)</h1>
    <p>QuillPeak IT WYSISYG text editor UI</p>
  </header>
</main>
</body>
</html>
```